Mass market mobile web site needs a designer

We need a web design for a mobile and tablet based site to be used as a second screen application usable by the mass market.

We would appreciate input not only into the graphical design aspects of the page but aslo the user experience aspects (UX) if possible. This is not an essential aspect of the brief however.

The design needs to be such that consumers can utilise the site's value with the least concentration possible as they will be wathcing the TV simultaneously.

The design should focus on the floating boxes (or similar) that will eventually move across the screen and the categories on the bottom of the screen. We need a design that somehow matches up the floating boxes with the category that the box is associated with.

Please refer to the attached wireframes for initial thoughts.

We would like the design to convey a friendly, inviting fun tone, perhaps even a little cheeky at times.

Reason: Some designers have requested that the deadline be extended.

Reason: No designs turning up.

Target Market(s)

Mass market TV viewers

Industry/Entity Type

Tv

Requirements
Must have
• It must work on smart phones and tablets in both landscape and portrait orientation. The end consumer must not feel intimidated by too many options on the page. It should feel fun, simple, obvious and non intrusive.
Nice to have
• Initial UX thoughts are demonstrated in the attached wireframes but alternative user experience ideas are welcome. For example, we have some doubts about whether a popup box is the best UX design and would be interested in other options that do not steal screen space.
Should not have
• It should not be cluttered, busy or intimidating. Users will not have their full attention on the screen. When their attention is focused on the screen it will be brief and actions on the screen should be very intuitive and simple.

```html
<!DOCTYPE html>
<html lang="en">
<head>
<meta charset="utf-8">
<title>Glimpse – second screen</title>
<link rel="stylesheet" href="https://fonts.googleapis.com/css2?family=Roboto:wght@400;500;700&display=swap">
<style>
:root{
  --page:#ffffff;
  --screen-top:#2a2a2a;
  --screen-bottom:#121212;
  --bar-light:#e6e6e6;
  --bar-mid:#b9b9b9;
  --chrome-top:#4a4a4a;
  --chrome-bottom:#1d1d1d;
  --chip:#3a3a3a;
  --chip-active:#151515;
  --ink-light:#f2f2f2;
  --ink-muted:#9a9a9a;
  --ink-status:#333333;
  --bubble:#ffffff;
  --bubble-ink:#8a8a8a;
  --accent-pink:#e0126e;
  --accent-link:#1a8fd6;
  --accent-blue:#34b3e4;
  --tab:#3b3b3b;
  --tab-raised:#555555;
  --icon-grey:#8c8c8c;
  --dialog:#151515;
  --dialog-edge:#8f8f8f;
  --button-top:#e8e8e8;
  --button-bottom:#bdbdbd;
  --star:#f5c400;
  --star-off:#777777;
  --salad-a:#9fbf4a;
  --salad-b:#d9a640;
}
*{box-sizing:border-box;margin:0;padding:0}
html,body{width:1200px;height:2397px;overflow:hidden;background:var(--page);font-family:"Roboto",sans-serif}
.screen{position:absolute;left:138px;width:924px;height:590px;overflow:hidden;
  background:linear-gradient(180deg,var(--screen-top),var(--screen-bottom));}
.screen--feed{top:118px}
.screen--alert{top:889px}
.screen--detail{top:1655px}

/* status bar */
.status-bar{position:absolute;left:0;top:0;width:100%;height:48px;
  background:linear-gradient(180deg,#f4f4f4,var(--bar-light) 50%,var(--bar-mid));
  color:var(--ink-status);font-weight:500}
.status-bar .carrier{position:absolute;left:14px;top:13px;font-size:20px;display:flex;align-items:flex-end;gap:10px}
.signal{display:flex;align-items:flex-end;gap:2px}
.signal i{display:block;width:4px;background:#2a7fd4}
.status-bar .app-name{position:absolute;left:0;right:0;top:9px;text-align:center;font-size:27px;color:#555}
.status-bar .clock{position:absolute;right:206px;top:12px;font-size:21px;font-weight:700}
.status-icons{position:absolute;right:12px;top:10px}

/* channel bar */
.channel-bar{position:absolute;left:0;top:48px;width:100%;height:86px;
  background:linear-gradient(180deg,var(--chrome-top),var(--chrome-bottom));
  display:flex;align-items:center;padding:0 4px;gap:3px}
.nav-btn{height:54px;display:flex;align-items:center;justify-content:center;color:var(--ink-light);
  font-size:24px;font-weight:700;background:linear-gradient(180deg,#4a4a4a,#262626);border:1px solid #5c5c5c}
.nav-btn--back{width:100px;clip-path:polygon(14px 0,100% 0,100% 100%,14px 100%,0 50%);padding-left:10px}
.nav-btn--next{width:96px;clip-path:polygon(0 0,calc(100% - 14px) 0,100% 50%,calc(100% - 14px) 100%,0 100%);padding-right:10px}
.channel{height:54px;display:flex;align-items:center;justify-content:center;gap:10px;color:var(--ink-light);
  font-size:19px;font-weight:500;background:var(--chip);border:1px solid #555}
.channel--active{background:var(--chip-active)}
.channel .mark{width:18px;height:18px;background:#cfcfcf;border-radius:50%}
.channel--active .mark{border-radius:0;background:#d12a2a}

/* floating boxes */
.float{position:absolute;display:flex;align-items:center}
.source{width:64px;display:flex;flex-direction:column;align-items:center;gap:4px;color:#ddd;font-size:14px;font-weight:500}
.source .dot{width:40px;height:40px;border-radius:50%;background:#e6e6e6}
.bubble{position:relative;margin-left:22px;background:var(--bubble);border-radius:3px;padding:9px 12px;
  font-size:12.5px;line-height:20px;color:var(--bubble-ink);width:232px;box-shadow:0 2px 4px rgba(0,0,0,.4)}
.bubble::before{content:"";position:absolute;left:-9px;top:50%;margin-top:-8px;
  border:8px solid transparent;border-right-color:var(--bubble);border-left:0;width:0;height:0}
.bubble .headline{color:var(--accent-pink)}
.bubble .link{color:var(--accent-link)}

/* tab bar */
.tab-bar{position:absolute;left:0;bottom:0;width:100%;height:100px;display:flex;align-items:flex-end}
.tab{height:100px;display:flex;flex-direction:column;align-items:center;justify-content:flex-end;padding-bottom:12px;
  gap:8px;color:#d6d6d6;font-size:18px;font-weight:500;background:linear-gradient(180deg,#464646,#262626);
  border-right:1px solid #191919;position:relative}
.tab--raised{height:110px;background:linear-gradient(180deg,#6a6a6a,#3a3a3a);border-radius:6px 6px 0 0;font-size:20px;color:#fff}
.tab .dot{width:46px;height:46px;border-radius:50%;background:var(--accent-blue)}
.tab .more{position:absolute;right:6px;top:6px;color:#888;font-size:22px;line-height:1}

/* dimmed dialog */
.dim{position:absolute;inset:0;background:rgba(0,0,0,.55)}
.dialog{position:absolute;left:261px;top:140px;width:438px;height:334px;background:var(--dialog);
  border:4px solid var(--dialog-edge);color:var(--ink-light)}
.dialog-title{height:72px;display:flex;align-items:center;gap:14px;padding-left:16px;font-size:32px;border-bottom:2px solid #4a4a4a}
.dialog-body{display:flex;gap:16px;padding:12px 8px 0}
.photo{flex:none;background:radial-gradient(circle at 45% 45%,var(--salad-b),var(--salad-a) 55%,#5c7f2a)}
.dialog-body .photo{width:135px;height:144px}
.dialog-text{font-size:17.5px;line-height:28px}
.dialog-text strong{color:var(--accent-blue)}
.dialog-actions{position:absolute;left:6px;right:6px;bottom:8px;display:flex;gap:8px}
.dialog-actions span{flex:1;height:60px;display:flex;align-items:center;justify-content:center;color:#222;font-size:20px;
  background:linear-gradient(180deg,var(--button-top),var(--button-bottom));border:1px solid #888}

/* detail screen */
.detail-header{position:absolute;left:0;top:0;width:100%;height:80px;
  background:linear-gradient(180deg,var(--chrome-top),var(--chrome-bottom));display:flex;align-items:center;padding-left:6px}
.detail-header .nav-btn--back{position:absolute;left:6px;top:13px}
.detail-title{position:absolute;left:232px;top:14px;width:460px;height:54px;border:2px solid #666;background:#2b2b2b;
  display:flex;align-items:center;justify-content:center;gap:16px;color:#fff;font-size:28px;font-weight:700}
.detail-main{position:absolute;left:24px;top:108px;display:flex;gap:18px;color:var(--ink-light)}
.detail-main .photo{width:169px;height:166px}
.meta .title{font-size:21px;margin-top:2px}
.meta .posted{font-size:13px;margin-top:2px}
.meta .series{font-size:21px;margin-top:22px}
.rating{display:flex;align-items:center;gap:10px;margin-top:6px;font-size:14px}
.stars{color:var(--star);font-size:23px;letter-spacing:1px}
.stars .off{color:var(--star-off)}
.meta .runtime{font-size:15px;font-weight:700;margin-top:6px}
.meta .tags{font-size:14px;margin-top:6px}
.meta .tags b{font-weight:400;margin-right:16px}
.synopsis{position:absolute;left:24px;top:336px;width:880px;color:var(--ink-light)}
.synopsis h2{font-size:20px;font-weight:700}
.synopsis p{font-size:14.5px;line-height:20px;margin-top:14px}
</style>
</head>
<body>

<!-- shared icon symbols -->
<svg width="0" height="0" style="position:absolute">
  <defs>
    <symbol id="hat" viewBox="0 0 40 44">
      <path d="M9 26c-5 0-8-4-8-8s3-8 8-8c1-5 6-9 11-9s10 4 11 9c5 0 8 4 8 8s-3 8-8 8v4H9z"/>
      <rect x="9" y="32" width="22" height="11" rx="1"/>
    </symbol>
    <symbol id="note" viewBox="0 0 40 40"><path d="M14 4l20-4v28a6 5 0 1 1-4-5V8l-12 3v21a6 5 0 1 1-4-5z"/></symbol>
    <symbol id="basket" viewBox="0 0 44 36"><path d="M4 14h36l-5 20H9z M12 14l8-12 M32 14l-8-12" fill="none" stroke="currentColor" stroke-width="3"/><path d="M14 18v12M22 18v12M30 18v12" stroke="currentColor" stroke-width="2"/></symbol>
    <symbol id="book" viewBox="0 0 48 34"><path d="M24 6C18 1 8 1 2 4v28c6-3 16-3 22 2 6-5 16-5 22-2V4C40 1 30 1 24 6z" fill="none" stroke="currentColor" stroke-width="3"/><path d="M24 6v28" stroke="currentColor" stroke-width="3"/></symbol>
    <symbol id="flower" viewBox="0 0 30 40"><path d="M5 2l5 6 5-6 5 6 5-6v10a10 10 0 0 1-20 0z"/><rect x="13" y="22" width="4" height="18"/><path d="M15 34c-6 0-10-4-12-8 6 0 10 3 12 8zM15 34c6 0 10-4 12-8-6 0-10 3-12 8z"/></symbol>
    <symbol id="plane" viewBox="0 0 44 44"><path d="M40 2c2 2 0 6-4 10l-6 6 5 20-4 4-8-16-7 7 1 7-3 3-3-7-7-3 3-3 7 1 7-7-16-8 4-4 20 5 6-6c4-4 8-6 10-4z"/></symbol>
    <symbol id="thumb" viewBox="0 0 20 20"><path d="M1 8h4v11H1zM7 8l4-7c2 0 3 1 2 4l-1 3h6c1 0 2 1 1 3l-3 8H7z"/></symbol>
  </defs>
</svg>

<!-- Screen 1: live feed -->
<section class="screen screen--feed">
  <header class="status-bar">
    <div class="carrier"><span class="signal"><i style="height:5px"></i><i style="height:8px"></i><i style="height:11px"></i><i style="height:14px"></i><i style="height:17px"></i></span>VELO 3G</div>
    <div class="app-name">Glimpse</div>
    <div class="clock">4:20 PM</div>
    <svg class="status-icons" width="186" height="28" viewBox="0 0 186 28">
      <circle cx="14" cy="14" r="10" fill="#777"/><path d="M14 8v6h5" stroke="#fff" stroke-width="2" fill="none"/>
      <path d="M46 4l14 6-7 2-2 8z" fill="#7a5fb4"/>
      <circle cx="96" cy="14" r="10" fill="none" stroke="#777" stroke-width="3"/>
      <rect x="128" y="6" width="44" height="18" rx="3" fill="none" stroke="#666" stroke-width="2"/><rect x="172" y="11" width="4" height="8" fill="#666"/><rect x="131" y="9" width="38" height="12" fill="#5cbf2a"/>
    </svg>
  </header>
  <nav class="channel-bar">
    <span class="nav-btn nav-btn--back">Back</span>
    <span class="channel channel--active" style="width:132px"><span class="mark"></span>Kite</span>
    <span class="channel" style="width:198px"><span class="mark"></span>Lumen</span>
    <span class="channel" style="width:180px"><span class="mark"></span>Ripple Channel</span>
    <span class="channel" style="width:186px"><span class="mark"></span>Harbor Channel</span>
    <span class="nav-btn nav-btn--next">Next</span>
  </nav>

  <div class="float" style="left:56px;top:180px"><div class="source"><span class="dot"></span>Chirper</div>
    <div class="bubble">Lorem ipsum dolor sit amet<br>@Glimpse: <span class="link">http://lnk.ex/Qe7Rm2Xa</span></div></div>
  <div class="float" style="left:465px;top:175px"><div class="source"><svg width="40" height="46" fill="#eee"><use href="#hat"/></svg></div>
    <div class="bubble"><span class="headline">Lorem ipsum dolor sit amet</span><br>co adipiscing elit enim ad minim.</div></div>
  <div class="float" style="left:100px;top:337px"><div class="source"><svg width="40" height="46" fill="#eee"><use href="#hat"/></svg></div>
    <div class="bubble"><span class="headline">Lorem ipsum dolor sit amet</span><br>co adipiscing elit enim ad minim.</div></div>
  <div class="float" style="left:498px;top:332px"><div class="source"><span class="dot"></span>Chirper</div>
    <div class="bubble">Lorem ipsum dolor sit amet<br>@Glimpse: <span class="link">http://lnk.ex/Qe7Rm2Xa</span></div></div>

  <nav class="tab-bar">
    <span class="tab" style="width:120px"><svg width="38" height="38" fill="var(--icon-grey)"><use href="#note"/></svg>Music</span>
    <span class="tab" style="width:125px"><svg width="42" height="36" color="var(--icon-grey)"><use href="#basket"/></svg>Shopping</span>
    <span class="tab tab--raised" style="width:146px"><span class="dot"></span>Chirper</span>
    <span class="tab" style="width:122px"><svg width="46" height="34" color="var(--icon-grey)"><use href="#book"/></svg>Books</span>
    <span class="tab" style="width:129px"><svg width="30" height="38" fill="var(--icon-grey)"><use href="#flower"/></svg>Gardening</span>
    <span class="tab tab--raised" style="width:146px"><svg width="44" height="48" fill="var(--accent-blue)"><use href="#hat"/></svg>Cooking</span>
    <span class="tab" style="width:136px"><span class="more">»</span><svg width="40" height="40" fill="var(--icon-grey)"><use href="#plane"/></svg>Traveling</span>
  </nav>
</section>

<!-- Screen 2: tip popup -->
<section class="screen screen--alert">
  <header class="status-bar">
    <div class="carrier"><span class="signal"><i style="height:5px"></i><i style="height:8px"></i><i style="height:11px"></i><i style="height:14px"></i><i style="height:17px"></i></span>VELO 3G</div>
    <div class="app-name">Glimpse</div>
    <div class="clock">4:20 PM</div>
    <svg class="status-icons" width="186" height="28" viewBox="0 0 186 28">
      <circle cx="14" cy="14" r="10" fill="#777"/><path d="M14 8v6h5" stroke="#fff" stroke-width="2" fill="none"/>
      <path d="M46 4l14 6-7 2-2 8z" fill="#7a5fb4"/>
      <circle cx="96" cy="14" r="10" fill="none" stroke="#777" stroke-width="3"/>
      <rect x="128" y="6" width="44" height="18" rx="3" fill="none" stroke="#666" stroke-width="2"/><rect x="172" y="11" width="4" height="8" fill="#666"/><rect x="131" y="9" width="38" height="12" fill="#5cbf2a"/>
    </svg>
  </header>
  <nav class="channel-bar">
    <span class="nav-btn nav-btn--back">Back</span>
    <span class="channel channel--active" style="width:132px"><span class="mark"></span>Kite</span>
    <span class="channel" style="width:198px"><span class="mark"></span>Lumen</span>
    <span class="channel" style="width:180px"><span class="mark"></span>Ripple Channel</span>
    <span class="channel" style="width:186px"><span class="mark"></span>Harbor Channel</span>
    <span class="nav-btn nav-btn--next">Next</span>
  </nav>

  <div class="float" style="left:56px;top:180px"><div class="source"><span class="dot"></span>Chirper</div>
    <div class="bubble">Lorem ipsum dolor sit amet<br>@Glimpse: <span class="link">http://lnk.ex/Qe7Rm2Xa</span></div></div>
  <div class="float" style="left:465px;top:175px"><div class="source"><svg width="40" height="46" fill="#eee"><use href="#hat"/></svg></div>
    <div class="bubble"><span class="headline">Lorem ipsum dolor sit amet</span><br>co adipiscing elit enim ad minim.</div></div>
  <div class="float" style="left:100px;top:337px"><div class="source"><svg width="40" height="46" fill="#eee"><use href="#hat"/></svg></div>
    <div class="bubble"><span class="headline">Lorem ipsum dolor sit amet</span><br>co adipiscing elit enim ad minim.</div></div>
  <div class="float" style="left:498px;top:332px"><div class="source"><span class="dot"></span>Chirper</div>
    <div class="bubble">Lorem ipsum dolor sit amet<br>@Glimpse: <span class="link">http://lnk.ex/Qe7Rm2Xa</span></div></div>

  <nav class="tab-bar">
    <span class="tab" style="width:120px"><svg width="38" height="38" fill="var(--icon-grey)"><use href="#note"/></svg>Music</span>
    <span class="tab" style="width:125px"><svg width="42" height="36" color="var(--icon-grey)"><use href="#basket"/></svg>Shopping</span>
    <span class="tab tab--raised" style="width:146px"><span class="dot"></span>Chirper</span>
    <span class="tab" style="width:122px"><svg width="46" height="34" color="var(--icon-grey)"><use href="#book"/></svg>Books</span>
    <span class="tab" style="width:129px"><svg width="30" height="38" fill="var(--icon-grey)"><use href="#flower"/></svg>Gardening</span>
    <span class="tab tab--raised" style="width:146px"><svg width="44" height="48" fill="var(--accent-blue)"><use href="#hat"/></svg>Cooking</span>
    <span class="tab" style="width:136px"><span class="more">»</span><svg width="40" height="40" fill="var(--icon-grey)"><use href="#plane"/></svg>Traveling</span>
  </nav>

  <div class="dim"></div>
  <div class="dialog">
    <div class="dialog-title"><svg width="40" height="44" fill="#fff"><use href="#hat"/></svg>Cooking Tips</div>
    <div class="dialog-body">
      <div class="photo" role="img" aria-label="Photo of a green salad with avocado and walnuts"></div>
      <p class="dialog-text"><strong>Lorem ipsum dolor sit amet</strong><br>consectetuer adipiscing elit, sed diam nonummy nibh euismod tincidunt ut laoreet.</p>
    </div>
    <div class="dialog-actions"><span>OK</span><span>Cancel</span></div>
  </div>
</section>

<!-- Screen 3: tip detail -->
<section class="screen screen--detail">
  <header class="detail-header">
    <span class="nav-btn nav-btn--back">Back</span>
    <div class="detail-title"><svg width="36" height="40" fill="#fff"><use href="#hat"/></svg>Cooking Tips on Demand</div>
  </header>
  <div class="detail-main">
    <div class="photo" role="img" aria-label="Photo of a green salad with avocado and walnuts"></div>
    <div class="meta">
      <div class="title">Lorem ipsum dolor sit amet</div>
      <div class="posted">Posted on 31/1/2013</div>
      <div class="series">COOKING TIPS On Demand</div>
      <div class="rating"><span class="stars">★★★★<span class="off">★</span></span>
        <svg width="20" height="20" fill="#ddd"><use href="#thumb"/></svg>240
        <svg width="20" height="20" fill="#ddd" style="transform:scaleY(-1)"><use href="#thumb"/></svg>20</div>
      <div class="runtime">2013 | 20 min</div>
      <div class="tags"><b>Tags:</b>Foods, Cooking, Cook, Health Food</div>
    </div>
  </div>
  <div class="synopsis">
    <h2>Cooking Tips On Demand</h2>
    <p>Lorem ipsum dolor sit amet, consectetuer adipiscing elit, sed diam nonummy nibh euismod tincidunt ut laoreet dolore magna aliquam erat volutpat.</p>
  </div>
  <nav class="tab-bar">
    <span class="tab" style="width:120px"><svg width="38" height="38" fill="var(--icon-grey)"><use href="#note"/></svg>Music</span>
    <span class="tab" style="width:125px"><svg width="42" height="36" color="var(--icon-grey)"><use href="#basket"/></svg>Shopping</span>
    <span class="tab tab--raised" style="width:146px"><span class="dot"></span>Chirper</span>
    <span class="tab" style="width:122px"><svg width="46" height="34" color="var(--icon-grey)"><use href="#book"/></svg>Books</span>
    <span class="tab" style="width:129px"><svg width="30" height="38" fill="var(--icon-grey)"><use href="#flower"/></svg>Gardening</span>
    <span class="tab tab--raised" style="width:146px"><svg width="44" height="48" fill="var(--accent-blue)"><use href="#hat"/></svg>Cooking</span>
    <span class="tab" style="width:136px"><span class="more">»</span><svg width="40" height="40" fill="var(--icon-grey)"><use href="#plane"/></svg>Traveling</span>
  </nav>
</section>

</body>
</html>
```